Powepoint Templates From Logo

Hello,

I am looking for a template for PowerPoint presentations for a new company selling Brivonlux's. The PowerPoint should keep the look and feel of our newly designed website ( which is still under development ) http://brivonlux.com/development/

I have attached our Logo which should be included in this template.
This PowerPoint will be used towards client during demonstrations and for internal use.

This template should be complete with fonts and colors of the text for both headlines and bullets/normal text.

I guess the easiest way for me to determine what I like is to see some dummy info/text on the submitted designs.

Thanks

Industry/Entity Type

It Company

Requirements
Must have
• Should include our logo

```html
<!DOCTYPE html>
<html lang="en">
<head>
<meta charset="utf-8">
<title>Brivonlux Presentation Template</title>
<link href="https://fonts.googleapis.com/css2?family=Roboto+Condensed:wght@400;700&display=swap" rel="stylesheet">
<style>
  :root {
    --header-dark: #4d6a00;
    --header-mid: #5f7f04;
    --header-light: #97b52a;
    --heading-green: #62822a;
    --bullet-green: #4f6e08;
    --body-grey: #6b6b6b;
    --footer-text: #2a2a2a;
    --page-white: #ffffff;
    --page-mist: #ececec;
    --photo-tone-a: #b9cfdc;
    --photo-tone-b: #c7d6b4;
  }
  * { margin: 0; padding: 0; box-sizing: border-box; }
  html, body { width: 1200px; height: 900px; overflow: hidden; }
  body {
    font-family: "Roboto Condensed", "Arial Narrow", sans-serif;
    background: var(--page-white);
  }
  .slide {
    position: relative;
    width: 1200px;
    height: 900px;
    overflow: hidden;
    background: linear-gradient(180deg, #f4f4f4 0%, var(--page-white) 30%, #f7f7f7 100%);
  }
  .slide-header {
    position: absolute;
    left: 0; top: 0;
    width: 1200px; height: 153px;
    background: linear-gradient(90deg, var(--header-dark) 0%, var(--header-mid) 55%, var(--header-light) 100%);
    border-bottom: 2px solid #dfe6cf;
  }
  .slide-title {
    position: absolute;
    left: 52px; top: 48px;
    font-size: 46px;
    line-height: 56px;
    font-weight: 700;
    color: var(--page-white);
  }
  .brand {
    position: absolute;
    left: 873px; top: 22px;
    display: flex;
    align-items: center;
    gap: 14px;
    height: 110px;
  }
  .brand-mark {
    width: 104px; height: 104px;
    border-radius: 50%;
    background: var(--page-white);
  }
  .brand-name {
    font-size: 44px;
    font-weight: 700;
    color: var(--page-white);
  }
  .content {
    position: absolute;
    left: 70px; top: 262px;
  }
  .content-heading {
    font-size: 42px;
    line-height: 52px;
    font-weight: 700;
    color: var(--heading-green);
    margin-bottom: 16px;
  }
  .bullet-list { list-style: none; }
  .bullet-list li {
    position: relative;
    padding-left: 36px;
    font-size: 27px;
    color: var(--body-grey);
    line-height: 60px;
    white-space: nowrap;
  }
  .bullet-list li::before {
    content: "";
    position: absolute;
    left: 6px; top: 22px;
    border-left: 14px solid var(--bullet-green);
    border-top: 8px solid transparent;
    border-bottom: 8px solid transparent;
  }
  .content-photo {
    position: absolute;
    left: 771px; top: 354px;
    width: 348px; height: 224px;
    border: 3px solid var(--page-white);
    border-radius: 6px;
    box-shadow: 0 2px 8px rgba(0,0,0,0.35);
    background: linear-gradient(135deg, var(--photo-tone-a) 0%, var(--photo-tone-b) 100%);
  }
  .slide-footer {
    position: absolute;
    left: 0; top: 803px;
    width: 1200px; height: 97px;
    background: linear-gradient(180deg, #fafafa 0%, var(--page-mist) 100%);
    border-top: 2px solid #e2e2e2;
  }
  .copyright {
    position: absolute;
    left: 57px; top: 37px;
    font-size: 24px;
    color: var(--footer-text);
  }
</style>
</head>
<body>
<main class="slide">
  <header class="slide-header">
    <h1 class="slide-title">Presentation Heading Here</h1>
    <div class="brand">
      <span class="brand-mark"></span>
      <span class="brand-name">Brivonlux</span>
    </div>
  </header>

  <section class="content">
    <h2 class="content-heading">Content Heading Here</h2>
    <ul class="bullet-list">
      <li>Sub Content Here Sub Content HereSub Content</li>
      <li>Sub Content Here Sub Content HereSub Content</li>
      <li>Sub Content Here Sub Content HereSub Content</li>
      <li>Sub Content Here Sub Content HereSub Content</li>
      <li>Sub Content Here Sub Content HereSub Content</li>
      <li>Sub Content Here Sub Content HereSub Content</li>
      <li>Sub Content Here Sub Content HereSub Content</li>
    </ul>
  </section>

  <div class="content-photo" role="img" aria-label="Photo of cupped hands holding a small green sapling outdoors"></div>

  <footer class="slide-footer">
    <p class="copyright">Copyright@Brivonlux</p>
  </footer>
</main>
</body>
</html>
```